Dorian Felsgrove breaking. Or D. Felsgrove breaking

I break in and train horses, any age any bread of horse, for any disaplin. I need a business card that is simple but effective, in the way of looking professional. I would like a horse on my card, preferably a horse without a rider. I also pre train horse, younge horses that need a bit of riding before they go into serious work, and prepare yearlings for sale.

Reason: This is for my boyfriend, and I really want it to be perfect and impressive!

Target Market(s)

Thoroughbred race horse trainers, horse industrie people.

Industry/Entity Type

Business

Contact Information for Business Card

Dorian Felsgrove horse breaking, "WOLBUNDA" Armidale, give your horse the right start to any career. dfels@quillmail.com.au, 0431862097. Horse breaking~pre-training~sale preparation

```html
<!DOCTYPE html>
<html lang="en">
<head>
<meta charset="utf-8">
<title>Dorian Felsgrove – Horse Breaking business card options</title>
<link rel="stylesheet" href="https://fonts.googleapis.com/css2?family=Berkshire+Swash&family=Carlito:wght@400;700&family=Kurale&display=swap">
<style>
  :root {
    --page: #ffffff;
    --ink: #111111;
    --photo-top: #6f5a63;
    --photo-mid: #8a7885;
    --photo-haze: #a595a6;
    --band: rgba(118, 110, 168, 0.78);
    --band-edge: rgba(150, 140, 196, 0.55);
    --foot-top: #3a3140;
    --foot-bottom: #1f1a24;
    --card-text: #ffffff;
  }
  html, body {
    margin: 0;
    padding: 0;
    width: 1200px;
    height: 422px;
    overflow: hidden;
    background: var(--page);
  }
  .sheet {
    position: relative;
    width: 1200px;
    height: 422px;
  }
  .option-number {
    position: absolute;
    top: 0;
    width: 589px;
    text-align: center;
    font-family: "Carlito", sans-serif;
    font-size: 46px;
    line-height: 50px;
    color: var(--ink);
  }
  .option-number--one { left: 0; }
  .option-number--two { left: 612px; }
  .card {
    position: absolute;
    top: 51px;
    width: 588px;
    height: 371px;
    overflow: hidden;
    color: var(--card-text);
    font-family: "Carlito", sans-serif;
  }
  .card--one { left: 0; }
  .card--two { left: 612px; }
  .card__photo {
    position: absolute;
    inset: 0;
    background:
      radial-gradient(ellipse at 75% 30%, var(--photo-haze) 0%, rgba(165,149,166,0) 55%),
      linear-gradient(180deg, var(--photo-top) 0%, var(--photo-mid) 45%, #7d7390 100%);
  }
  .card__tagline {
    position: absolute;
    left: 0;
    right: 0;
    top: 116px;
    text-align: center;
    font-size: 22px;
    line-height: 28px;
  }
  .card--one .card__tagline { font-family: "Berkshire Swash", cursive; }
  .card--two .card__tagline { font-family: "Kurale", serif; font-size: 23px; }
  .card__band {
    position: absolute;
    left: 0;
    right: 0;
    top: 153px;
    height: 161px;
    background: linear-gradient(90deg, var(--band) 0%, var(--band) 55%, var(--band-edge) 100%);
  }
  .card__name {
    position: absolute;
    left: 32px;
    top: 178px;
    font-size: 27px;
    line-height: 30px;
  }
  .card--two .card__name { font-weight: 700; font-size: 26px; }
  .card__role {
    position: absolute;
    left: 32px;
    top: 211px;
    font-size: 20px;
    line-height: 24px;
  }
  .card--two .card__role { font-size: 18px; }
  .card__contact {
    position: absolute;
    right: 34px;
    top: 219px;
    text-align: right;
    font-size: 18px;
    line-height: 25px;
  }
  .card__contact-line {
    display: flex;
    justify-content: flex-end;
    align-items: center;
    gap: 4px;
  }
  .card__icon { width: 15px; height: 15px; }
  .card__footer {
    position: absolute;
    left: 0;
    right: 0;
    top: 314px;
    height: 57px;
    background: linear-gradient(180deg, var(--foot-top), var(--foot-bottom));
    text-align: center;
    font-size: 22px;
    line-height: 57px;
  }
  .card--one .card__footer { font-family: "Berkshire Swash", cursive; font-size: 21px; }
  .card--two .card__footer { font-size: 24px; }
</style>
</head>
<body>
<main class="sheet">
  <div class="option-number option-number--one">1</div>
  <div class="option-number option-number--two">2</div>

  <section class="card card--one">
    <div class="card__photo" role="img" aria-label="Photograph of a group of horses standing in soft morning mist"></div>
    <p class="card__tagline" style="margin:0">give your horse the right start to any career</p>
    <div class="card__band"></div>
    <div class="card__name">Dorian Felsgrove</div>
    <div class="card__role">Horse breaking</div>
    <div class="card__contact">
      <div class="card__contact-line">"WOLBUNDA" Armidale,</div>
      <div class="card__contact-line">
        <svg class="card__icon" viewBox="0 0 16 16" aria-hidden="true"><rect x="5" y="4" width="7" height="11" rx="3.5" fill="none" stroke="#fff" stroke-width="1.2"/><line x1="8.5" y1="4" x2="8.5" y2="8" stroke="#fff" stroke-width="1"/><path d="M8.5 4 C8 1, 4 2, 2 1" fill="none" stroke="#fff" stroke-width="1"/></svg>:&nbsp;dfels@quillmail.com.au
      </div>
      <div class="card__contact-line">
        <svg class="card__icon" viewBox="0 0 16 16" aria-hidden="true"><path d="M4 2 L7 2 L7 5 L5.5 6 C6 8.5 7.5 10 10 10.5 L11 9 L14 9 L14 12 C14 13 13 14 12 14 C7 14 2 9 2 4 C2 3 3 2 4 2 Z" fill="#fff"/></svg>:&nbsp;0431862097
      </div>
    </div>
    <div class="card__footer">Horse breaking – Pre-training – Sale preparation</div>
  </section>

  <section class="card card--two">
    <div class="card__photo" role="img" aria-label="Photograph of a group of horses standing in soft morning mist"></div>
    <p class="card__tagline" style="margin:0">give your horse the right start to any career</p>
    <div class="card__band"></div>
    <div class="card__name">Dorian Felsgrove</div>
    <div class="card__role">Horse breaking</div>
    <div class="card__contact">
      <div class="card__contact-line">"WOLBUNDA" Armidale,</div>
      <div class="card__contact-line">E : dfels@quillmail.com.au</div>
      <div class="card__contact-line">T : 0431862097</div>
    </div>
    <div class="card__footer">Horse breaking - Pre-training - Sale preparation</div>
  </section>
</main>
</body>
</html>
```